Awesome ecommerce store banner needed!

We need a sharp, clear, strong banner for one of our subcategory pages on http://www.brixmolt.com
We'd like to incorporate the following image. We'd like the background to be gray or black. We are replacing the Wireless Intercoms banner that is orange (we hate it).
WE do like our other banners, however, so please use them as reference:
SIze: 980 x 380
Two raw images of the intercom we'd like you to encorporate have been included. Choose one or the other depending on what you think would be best. If using the single angle, please duplicate it. We want two intercoms in the banner
Simple and Clean is key:
Text: Wireless Intercoms
Text Color: Can be white/off gray
Text Style: Please keep it clean in line with the website
Background: Black/gray/white

```html
<!DOCTYPE html>
<html lang="en">
<head>
<meta charset="utf-8">
<title>Wireless Intercoms</title>
<link rel="stylesheet" href="https://fonts.googleapis.com/css2?family=Roboto:wght@700;900&display=swap">
<style>
  :root {
    --bg-black: #050505;
    --bg-charcoal: #1c1c1c;
    --sweep-gray: #3a3a3a;
    --title-white: #ffffff;
    --title-silver: #b9b9b9;
    --device-silver: #d8d8d8;
    --device-shadow: #7d7d7d;
    --device-black: #161616;
  }
  html, body {
    margin: 0;
    padding: 0;
    overflow: hidden;
    background: var(--bg-black);
  }
  .banner {
    position: relative;
    width: 1200px;
    height: 465px;
    overflow: hidden;
    background: var(--bg-black);
  }
  .banner-backdrop {
    position: absolute;
    inset: 0;
  }
  .product-area {
    position: absolute;
  }
  .product-area--rear {
    left: 37px;
    top: 12px;
    width: 290px;
    height: 196px;
  }
  .product-area--front {
    left: 66px;
    top: 90px;
    width: 438px;
    height: 316px;
  }
  .banner-title {
    position: absolute;
    left: 530px;
    top: 52px;
    width: 620px;
    height: 250px;
    font-family: "Roboto", "Helvetica Neue", Arial, sans-serif;
    font-weight: 900;
  }
</style>
</head>
<body>
<div class="banner">
  <svg class="banner-backdrop" width="1200" height="465" viewBox="0 0 1200 465" aria-hidden="true">
    <defs>
      <radialGradient id="glow-center" cx="560" cy="250" r="520" gradientUnits="userSpaceOnUse">
        <stop offset="0" stop-color="var(--bg-charcoal)"/>
        <stop offset="1" stop-color="var(--bg-black)"/>
      </radialGradient>
      <linearGradient id="sweep" x1="0" y1="0" x2="1" y2="0">
        <stop offset="0" stop-color="var(--sweep-gray)" stop-opacity="0"/>
        <stop offset="0.55" stop-color="var(--sweep-gray)" stop-opacity="0.55"/>
        <stop offset="1" stop-color="var(--sweep-gray)" stop-opacity="0.15"/>
      </linearGradient>
    </defs>
    <rect width="1200" height="465" fill="url(#glow-center)"/>
    <path d="M0 465 C 200 330, 620 300, 1200 360 L1200 380 C 640 320, 230 350, 40 465 Z" fill="url(#sweep)"/>
    <path d="M520 0 C 700 120, 900 170, 1200 170 L1200 150 C 920 150, 740 100, 580 0 Z" fill="url(#sweep)" opacity="0.6"/>
    <ellipse cx="300" cy="300" rx="330" ry="170" fill="none" stroke="var(--sweep-gray)" stroke-opacity="0.35" stroke-width="2"/>
  </svg>

  <div class="product-area product-area--rear" role="img" aria-label="Photo of a silver and black wireless intercom unit with antenna, seen from behind">
    <svg width="290" height="196" viewBox="0 0 290 196" aria-hidden="true">
      <defs>
        <linearGradient id="rear-body" x1="0" y1="0" x2="1" y2="1">
          <stop offset="0" stop-color="var(--device-silver)"/>
          <stop offset="0.55" stop-color="var(--device-shadow)"/>
          <stop offset="1" stop-color="var(--device-black)"/>
        </linearGradient>
      </defs>
      <path d="M0 110 L200 70 L288 120 L90 175 Z" fill="url(#rear-body)" opacity="0.9"/>
    </svg>
  </div>

  <div class="product-area product-area--front" role="img" aria-label="Photo of a silver and black wireless intercom unit with antenna, talk button and channel selector">
    <svg width="438" height="316" viewBox="0 0 438 316" aria-hidden="true">
      <defs>
        <linearGradient id="front-body" x1="0" y1="0" x2="1" y2="1">
          <stop offset="0" stop-color="var(--device-silver)"/>
          <stop offset="0.5" stop-color="var(--device-shadow)"/>
          <stop offset="0.8" stop-color="var(--device-black)"/>
        </linearGradient>
      </defs>
      <path d="M0 150 L280 80 L436 170 L150 250 Z" fill="url(#front-body)" opacity="0.9"/>
    </svg>
  </div>

  <svg class="banner-title" viewBox="0 0 620 250" role="heading" aria-level="1" aria-label="Wireless Intercoms">
    <defs>
      <linearGradient id="title-fill" x1="0" y1="0" x2="0" y2="1">
        <stop offset="0" stop-color="var(--title-white)"/>
        <stop offset="0.55" stop-color="var(--title-white)"/>
        <stop offset="1" stop-color="var(--title-silver)"/>
      </linearGradient>
    </defs>
    <text x="14" y="118" font-size="144" textLength="582" lengthAdjust="spacingAndGlyphs" fill="url(#title-fill)">WIRELESS</text>
    <text x="8" y="236" font-size="144" textLength="594" lengthAdjust="spacingAndGlyphs" fill="url(#title-fill)">INTERCOMS</text>
  </svg>
</div>
</body>
</html>
```